Design Tweak needed for a current site

Design on top of an existing quiz funnel

Ideally we would like to tweak what we have already built here (moving elements, styles, adding simple elements etc): http://offers.plumrivetdeals.com/can-you-save-on-car-insurance

The flow:
1) User lands on the quiz page
2) User answers X questions and moves through the flow
3) Calculating user results screen
4) User reaches a success screen, and is subsequently redirected

Keys to the design:
1) We need to emphasize the quiz title as that will drive engagement. In this case, this is a quiz to see if you might be eligible to save money on car insurance.

2) At the end of the quiz we need to make it very, very clear that the user is eligible for savings and that in order to complete the process they are being redirected to another page where they need to fill out a form. It is critical that the design communicates this very clearly... We can count down the time left until redirect and we can use any order of elements to make this point. I think our current design does a very bad job of this.

3) We want to have a "calculating" step so that it seems like the page is working in the background

Goals of the design:
1) Polished, high quality experience throughout
2) User is clearly prepared to be redirected to the conversion funnel/landing page at the end
3) User understands the value of completing the quiz

Target Market(s)

designers

Industry/Entity Type

Moving

Number of Pages Required

1 page

Font styles to use
Sans Serif

Colors

Designer to choose colors to be used in the design.

Requirements
Must have
• This quiz funnel is a template so while the current use case is for auto insurance, we would like a design that also would work in other contexts.
Should not have
• We don't want to materially change the core functionality of the quiz itself... redesigning any of the elements or interactions is encouraged though

```html
<!DOCTYPE html>
<html lang="en">
<head>
<meta charset="utf-8">
<title>QuoteHarbor – Car Insurance Quiz</title>
<link href="https://fonts.googleapis.com/css2?family=Poppins:wght@400;500;600;700&display=swap" rel="stylesheet">
<style>
  :root{
    --ink:#222;
    --text:#454545;
    --muted:#5a5a5a;
    --yellow:#fdc64f;
    --teal:#9fd8cf;
    --teal-dark:#7fcabd;
    --green:#7fb51b;
    --green-light:#9ccf2f;
    --card:#f2f2f2;
    --card-border:#ffffff;
    --bar:#fafafa;
    --bg-center:#ffffff;
    --bg-edge:#dcdcdc;
  }
  *{margin:0;padding:0;box-sizing:border-box}
  html,body{width:1200px;height:771px;overflow:hidden}
  body{font-family:'Poppins',sans-serif;color:var(--text);position:relative;background:var(--bg-edge)}
  .backdrop{position:absolute;inset:0;background:radial-gradient(ellipse 520px 420px at 600px 330px,var(--bg-center) 0%,#f1f1f1 55%,var(--bg-edge) 100%)}
  .scene-left,.scene-right{position:absolute;border-radius:20px;background:linear-gradient(180deg,rgba(200,200,200,.35),rgba(200,200,200,.1))}
  .scene-left{left:0;top:70px;width:400px;height:290px}
  .scene-right{left:780px;top:10px;width:420px;height:320px}
  .pillar{position:absolute;left:1018px;top:333px;width:74px;height:438px;background:linear-gradient(90deg,#c9c9c9,#d6d6d6)}
  .brand{position:absolute;top:54px;left:0;width:1200px;display:flex;justify-content:center;align-items:center;gap:10px}
  .brand-dot{width:40px;height:40px;border-radius:50%;background:var(--ink)}
  .brand-name{font-size:34px;font-weight:500;color:var(--ink);letter-spacing:.5px}
  .quiz-badge{position:absolute;left:536px;top:169px;width:128px;height:39px;background:var(--yellow);border-radius:20px;font-weight:700;font-size:26px;color:#222;text-align:center;line-height:40px}
  .quiz-badge::after{content:"";position:absolute;left:60px;bottom:-12px;border-left:10px solid var(--yellow);border-right:4px solid transparent;border-bottom:12px solid transparent}
  .headline{position:absolute;top:238px;width:1200px;text-align:center;font-size:26px;color:var(--text)}
  .tagline{position:absolute;left:258px;top:303px;width:684px;height:31px;background:var(--teal);border-radius:3px;font-size:15px;font-weight:500;color:#2b4a45;text-align:center;line-height:31px}
  .step-tab{position:absolute;left:511px;top:373px;width:180px;height:36px;background:#ebebeb;clip-path:polygon(10% 0,90% 0,100% 100%,0 100%);border-radius:10px 10px 0 0;text-align:center;font-size:17px;line-height:36px;color:var(--muted)}
  .progress{position:absolute;left:194px;top:408px;width:813px;height:33px;border-radius:17px;background:var(--bar);border:2px solid #e2e2e2;box-shadow:inset 0 2px 4px rgba(0,0,0,.08)}
  .progress-fill{position:absolute;left:5px;top:5px;width:147px;height:19px;border-radius:10px;background:repeating-linear-gradient(135deg,var(--green) 0 3px,var(--green-light) 3px 6px)}
  .question{position:absolute;top:474px;width:1200px;text-align:center;font-size:24px;color:var(--text)}
  .shelf{position:absolute;left:94px;top:688px;width:1012px;height:22px;background:linear-gradient(180deg,#fafafa,#d8d8d8);box-shadow:0 12px 14px -6px rgba(0,0,0,.35)}
  .answer{position:absolute;top:537px;width:141px;height:157px;background:var(--card);border:3px solid var(--card-border);border-radius:4px;box-shadow:0 0 0 1px #d4d4d4,0 4px 8px rgba(0,0,0,.08);text-align:center}
  .answer-lease{left:446px}
  .answer-own{left:613px}
  .answer-icon{position:absolute;left:35px;top:26px;width:66px;height:68px;border-radius:6px;background:linear-gradient(135deg,var(--teal),var(--teal-dark))}
  .answer-label{position:absolute;left:0;top:106px;width:100%;font-size:21px;color:var(--text)}
</style>
</head>
<body>
  <div class="backdrop"></div>
  <div class="scene-left" role="img" aria-label="Faint line illustration of a car with money, calculator and savings icons"></div>
  <div class="scene-right" role="img" aria-label="Faint line illustration of a hand holding a car surrounded by insurance coverage icons"></div>
  <div class="pillar"></div>

  <header class="brand">
    <span class="brand-dot"></span>
    <span class="brand-name">QuoteHarbor</span>
  </header>

  <div class="quiz-badge">QUIZ</div>
  <h1 class="headline" style="font-weight:400">Are You Overpaying For Car Insurance?</h1>
  <p class="tagline">Take our five question quiz to see if you might be eligible for car insurance savings</p>

  <div class="step-tab">Question 1/2</div>
  <div class="progress"><div class="progress-fill"></div></div>

  <h2 class="question" style="font-weight:400">Do you Lease Or Own:</h2>

  <div class="shelf"></div>
  <div class="answer answer-lease">
    <div class="answer-icon" role="img" aria-label="Lease document icon with a car"></div>
    <div class="answer-label">I Lease!</div>
  </div>
  <div class="answer answer-own">
    <div class="answer-icon" role="img" aria-label="Owned car icon with a dollar coin"></div>
    <div class="answer-label">I Own!</div>
  </div>
</body>
</html>
```